Professional business cards for real estate development company

I need business cards for my new real estate development company. The company, "KORVA" is a real estate development, investment, and advisory firm with a focus on multifamily, office, and mixed-use projects across primary and secondary markets in the Southeast United States.

Style preference is modern

Industry/Entity Type

Real Estate Development

Contact Information for Business Card

The business cards need to include:
Name
Title
Mailing Address
Phone Number
Web Address

Logo is attached. I would like white to be the primary color with incorporation of the company colors: #232D3A and #B5A451

Font styles to use
Other font styles liked:
• Montserrat, Avenir

Requirements
Must have
• Company Logo. No need to include the company name since the name is in the logo.
Should not have
• No line type designs

```html
<!DOCTYPE html>
<html lang="en">
<head>
<meta charset="UTF-8">
<title>KORVA Business Cards</title>
<link href="https://fonts.googleapis.com/css2?family=Montserrat:wght@400;500;600;700&display=swap" rel="stylesheet">
<style>
  :root {
    --navy: #232D3A;
    --gold: #B5A451;
    --paper: #FFFFFF;
    --backdrop: #C9C9C9;
    --faint: #EEEEEE;
  }
  * { margin: 0; padding: 0; box-sizing: border-box; }
  html, body { width: 1200px; height: 900px; overflow: hidden; }
  body {
    background: var(--backdrop);
    font-family: "Montserrat", sans-serif;
    color: var(--navy);
    display: flex;
    flex-direction: column;
    align-items: center;
    justify-content: center;
    gap: 40px;
  }
  .card {
    width: 700px;
    height: 400px;
    background: var(--paper);
    position: relative;
    box-shadow: 0 6px 18px rgba(0,0,0,0.18);
  }

  /* Back side */
  .card-back .mark-area {
    position: absolute;
    left: 90px; top: 70px;
    width: 260px; height: 260px;
    background: var(--faint);
  }
  .card-back .tagline {
    position: absolute;
    right: 60px; top: 150px;
    text-align: right;
    padding-right: 16px;
    border-right: 4px solid var(--gold);
    font-weight: 600;
    font-size: 22px;
    line-height: 1.25;
    letter-spacing: 0.5px;
  }

  /* Front side */
  .card-front .brand {
    position: absolute;
    left: 70px; top: 150px;
    display: flex;
    align-items: center;
    gap: 14px;
  }
  .brand-square {
    width: 34px; height: 34px;
    background: var(--navy);
  }
  .brand-name {
    font-weight: 700;
    font-size: 44px;
    letter-spacing: 3px;
    color: var(--navy);
  }
  .divider {
    position: absolute;
    left: 350px; top: 70px;
    width: 2px; height: 200px;
    background: var(--gold);
  }
  .contact {
    position: absolute;
    left: 380px; top: 78px;
  }
  .person-name {
    color: var(--gold);
    font-weight: 700;
    font-size: 22px;
    letter-spacing: 0.5px;
  }
  .person-title {
    font-weight: 500;
    font-size: 14px;
    letter-spacing: 1px;
    margin-top: 2px;
  }
  .contact-list {
    list-style: none;
    margin-top: 28px;
    font-size: 15px;
    line-height: 1.75;
  }
  .contact-list li { display: flex; align-items: center; gap: 8px; }
  .contact-list svg { width: 14px; height: 14px; flex: none; }
  .address {
    position: absolute;
    left: 0; right: 0; bottom: 44px;
    text-align: center;
    font-size: 16px;
    font-weight: 500;
  }
</style>
</head>
<body>
  <section class="card card-back">
    <div class="mark-area" role="img" aria-label="Faint company mark decoration"></div>
    <p class="tagline">COMMERCIAL<br>REAL ESTATE PLATFORM</p>
  </section>

  <section class="card card-front">
    <div class="brand">
      <span class="brand-square"></span>
      <span class="brand-name">KORVA</span>
    </div>
    <div class="divider"></div>
    <div class="contact">
      <p class="person-name">DANIEL REYES</p>
      <p class="person-title">PARTNER</p>
      <ul class="contact-list">
        <li>
          <svg viewBox="0 0 16 16"><path d="M3 1.5l3 .5 1 3-2 1.5a9 9 0 0 0 4.5 4.5L11 9l3 1 .5 3-2 1.5C7 14 2 9 1.5 3.5z" fill="var(--gold)"/></svg>
          (555) 014-2280
        </li>
        <li>
          <svg viewBox="0 0 16 16"><rect x="1" y="3" width="14" height="10" fill="none" stroke="var(--gold)" stroke-width="1.6"/><path d="M1 3l7 6 7-6" fill="none" stroke="var(--gold)" stroke-width="1.6"/></svg>
          info@korvadevelopment.com
        </li>
        <li>
          <svg viewBox="0 0 16 16"><circle cx="8" cy="8" r="6.5" fill="none" stroke="var(--gold)" stroke-width="1.5"/><path d="M1.5 8h13M8 1.5c-3 3.5-3 9.5 0 13M8 1.5c3 3.5 3 9.5 0 13" fill="none" stroke="var(--gold)" stroke-width="1.2"/></svg>
          www.korvadevelopment.com
        </li>
      </ul>
    </div>
    <p class="address">4120 Calder Street NE, Atlanta, Georgia 30309</p>
  </section>
</body>
</html>
```